Velmora Outcomes Brochure Design Project

- Who we are?
Velmora Outcomes is New Internet Marketing Company Based in China.

It is our aim to provide Chinese clients with the means to internationally market their product, via the Internet.

Our primary products are Outsourced Design ( Thanks to Pixel hive and the amazing designers who use it), SEO and Virtual Hosting.

- Project Brief
Design a vibrant and fresh brochure that introduces the fundamentals of SEO. There is no restriction to the number of pages, however all the info I have included in this brief must be included.

- Colour Palette
Please see link or download the Adobe Swatch Exchange File or follow the link below
http://tintaro.example.com/#themes/search?term=5830716
Updates

Logo updated - grey background removed

Various file formats added for logo and brochure content

Brochure zip file add containing logo in different formats.

Adobe color scheme file added

The general corporate colors are:

Base Color: CMYK :0, 60, 80, 0  Hex: FF6633
Dark Orange: CMYK: 0, 72, 96, 30 Hex: B23308
Light Orange: CMYK 0, 42, 56, 0 Hex: FF9571
Grey: CMYK 0, 0, 0, 48 Hex: 858585
Light Grey: CMYK 0, 0, 0, 26 Hex: BDBDBD

Please note that I'm happy for other colors to be included, however I would like these the corporate branding colors to be clearly present through the brochure.

Hi All

First place payment has increased to $600 - Looking to see some creative designs!

Hi All

Project Deadline Extended
Reason: I have increase the budget and extend the deadline as I need to see more design.

I have attached a zip file that contains example brochures I like.

We are not keen on the table data its a little plain. We have create an info-graphic to replace one of the table and would like to see it included in the design.

Project Deadline Extended
Reason: A few designers have asked for this extension and I would like to see additional designs. Thanks Marek

Target Market(s)

- Our Target Audience is..
It is small to medium businesses looking to reach out to the international market.
Our clients still very much operate on a face to face level in business and are new to the concept of Internet marketing

However this must look professional, Marketable and Clean, with the power of connecting people globally, through SEO and design to be reflected visually in the brochure.

Industry/Entity Type

Internet

Requirements
Must have
• One or more of the FACTS that I have highlighted need to stand out on each page. These FACTS can be found the document attached to this brief and are under the section titled 'Did You Know!'. Not every fact in this section needs to be highlighted in the brochure, but each page needs to have at least, one or more fact that stands out, soemwhere on the page.
See attached document, under the heading 'Did you Know!' and use one or two of these facts to spruce up the pages!

One image/ per page or per two pages MUST be included!

- Provide stock photos and please send us a message with the additional cost of these with your submission

The Table data, that I have included in the attachment must be included in the body of the pages - BUT the table format is not necessary and you can place the information in the body like plain text.

The brochure size should be a little larger than A4.

Please design the back page, like a pocket to hold paper and other material in it that I include with this brochure.

```html
<!DOCTYPE html>
<html lang="en">
<head>
<meta charset="utf-8">
<title>Velmora Outcomes – Online Marketing and SEO vs Traditional</title>
<link rel="stylesheet" href="https://fonts.googleapis.com/css2?family=Open+Sans:wght@400;600&display=swap">
<style>
  :root {
    --base-orange: #FF6633;
    --dark-orange: #B23308;
    --light-orange: #FF9571;
    --grey: #858585;
    --light-grey: #BDBDBD;
    --cell-border: #efbba3;
    --header-fill: #fbe4d8;
    --label-fill: #fce9e0;
    --cell-fill: #fdf5f1;
    --ink: #2f2f2f;
    --page: #ffffff;
  }
  html, body {
    margin: 0;
    padding: 0;
    overflow: hidden;
    background: var(--page);
  }
  .page {
    position: relative;
    width: 863px;
    height: 1200px;
    background: var(--page);
    font-family: "Open Sans", sans-serif;
    color: var(--ink);
    overflow: hidden;
  }
  .brand {
    position: absolute;
    top: 30px;
    right: 22px;
    display: flex;
    align-items: center;
    gap: 14px;
  }
  .brand-name {
    font-size: 20px;
    font-weight: 600;
    color: var(--base-orange);
  }
  .brand-dot {
    width: 132px;
    height: 132px;
    border-radius: 50%;
    background: var(--base-orange);
  }
  .comparison {
    position: absolute;
    top: 266px;
    left: 31px;
    width: 809px;
    border-collapse: collapse;
    table-layout: fixed;
    font-size: 13.5px;
    line-height: 1.5;
  }
  .comparison th,
  .comparison td {
    border: 1px solid var(--cell-border);
    padding: 6px 8px;
    vertical-align: middle;
    text-align: left;
    background: var(--cell-fill);
    font-weight: 400;
  }
  .comparison thead th {
    background: var(--header-fill);
    height: 16px;
  }
  .comparison .criterion {
    background: var(--label-fill);
  }
  .row-cost { height: 106px; }
  .row-roi { height: 100px; }
  .row-availability { height: 114px; }
  .row-time { height: 180px; }
  .row-target { height: 140px; }
  .row-feedback { height: 195px; }
</style>
</head>
<body>
<div class="page">
  <div class="brand">
    <span class="brand-name">Velmora Outcomes</span>
    <span class="brand-dot"></span>
  </div>

  <table class="comparison">
    <colgroup>
      <col style="width:113px">
      <col style="width:62px">
      <col style="width:303px">
      <col style="width:172px">
      <col style="width:159px">
    </colgroup>
    <thead>
      <tr>
        <th colspan="3">Online Marketing and SEO</th>
        <th colspan="2">Traditional???</th>
      </tr>
    </thead>
    <tbody>
      <tr class="row-cost">
        <th class="criterion" scope="row">Cost</th>
        <td>Low Cost</td>
        <td>SEO cost are lower that traditional marketing cost and reach an international audience</td>
        <td>High Cost</td>
        <td>Human Resources costs a lot of money Media coverages costs a lot of money</td>
      </tr>
      <tr class="row-roi">
        <th class="criterion" scope="row">Return On Investment</th>
        <td>Low Risk/ High Return</td>
        <td>Due to its low implementation costs, SEO has a very high return on investment (ROI). This reduces the risk you need to take to maintain or increase profits</td>
        <td>High Risk/ Low to Medium Return</td>
        <td>Traditional Marketing involves high up-front costs that may never return your original investment.</td>
      </tr>
      <tr class="row-availability">
        <th class="criterion" scope="row">Availability to Business</th>
        <td>Any size business</td>
        <td>Due to low cost and high return SEO is availabe to any business</td>
        <td>Medium to large corporations</td>
        <td>Due to media costs it is virtual impossible to get vide national coverage for a small company</td>
      </tr>
      <tr class="row-time">
        <th class="criterion" scope="row">Time required</th>
        <td>Low</td>
        <td>Imagine your business running 24 hours day. With SEO, potential customers can visit you website from anywhere at any time. They can even purchase goods whilst you're asleep. With online marketing we can personalize automated emails to entice more pruchase</td>
        <td>High</td>
        <td>Direct marketing requires a physical person to be interacting with the customer and even the best sales man can't do this 24 hours a day</td>
      </tr>
      <tr class="row-target">
        <th class="criterion" scope="row">Ability to target audience</th>
        <td>Easy</td>
        <td>By its very nature SEO only targets those that are interested in your field or product - the bonus is that your audience is from all over the world</td>
        <td>Difficult and costly</td>
        <td>Traditional media is limited to either a small target audience or a wide non-targeted audience. Internet marketing allows both</td>
      </tr>
      <tr class="row-feedback">
        <th class="criterion" scope="row">Change marketing based on feedback</th>
        <td>Very Simple</td>
        <td>Internet marketing is all about helping you tailoring and automating what the consumer sees, based on feedback, to increase your return on investment</td>
        <td></td>
        <td>Traditional marketing takes time to update and distribute even in best case senario you have to update your brochure and get it print</td>
      </tr>
    </tbody>
  </table>
</div>
</body>
</html>
```